Quick & Dirty Poster Design Project - A2 Posters

I run a business called Brindle Terrace. We sell high end outdoor flooring and walling (natural stone products) to architects and designers.

We work mainly with high end landscape designers on garden design and outdoor architecture.

Our sales teams provide advice and expertise and sell architectural design products to architects and designers.

I wanted to design some fun A2 posters to put in the sales offices just to create a bit of energy and momentum for staff. These are for internal use only.

The 4 copy lines are:

1.Beware of people who don't get their hands dirty

2. If you don't take a chance you won't have one

3. Having trouble getting started? Quit talking and start doing

4. Remember the questions you ask are more important than anything you could ever say

Just one copy line for each poster

(Pls note due to the limited budget and timings, I'm expecting interesting typeset posters not "designed" artworks). Thanks

Target Market(s)

sales team

Industry/Entity Type

Landscape

Requirements
Must have
• Our logo (Brindle Terrace) - I have provided a few versions of the logo
Nice to have
• Some design element alongside the typeface / copy

```html
<!DOCTYPE html>
<html lang="en">
<head>
<meta charset="utf-8">
<title>Brindle Terrace – Quit talking and start doing</title>
<link rel="stylesheet" href="https://fonts.googleapis.com/css2?family=Roboto+Condensed:wght@300;700&display=swap">
<style>
  :root {
    --pink-top: #eba6bc;
    --pink-mid: #de7090;
    --deep-red: #8e1d22;
    --red-low: #c22b3e;
    --red-base: #d42f44;
    --lime: #b6d335;
    --white: #ffffff;
  }
  html, body {
    margin: 0;
    padding: 0;
    width: 849px;
    height: 1200px;
    overflow: hidden;
  }
  .poster {
    position: relative;
    width: 849px;
    height: 1200px;
    background: linear-gradient(to bottom,
      var(--pink-top) 0%,
      var(--pink-mid) 28%,
      #b94a5c 42%,
      var(--deep-red) 53%,
      #a8262f 62%,
      var(--red-low) 78%,
      var(--red-base) 100%);
    font-family: "Roboto Condensed", "Arial Narrow", sans-serif;
    color: var(--white);
  }
  .headline {
    position: absolute;
    left: 203px;
    top: 86px;
    margin: 0;
    font-size: 98px;
    line-height: 89px;
    letter-spacing: -2px;
  }
  .headline span { display: block; }
  .question { font-weight: 300; }
  .action { font-weight: 700; }
  .connector { font-weight: 300; }
  .marker {
    position: absolute;
    left: 133px;
  }
  .marker-square { top: 515px; }
  .marker-arrow { top: 783px; }
  .brand {
    position: absolute;
    right: 76px;
    top: 955px;
    font-weight: 700;
    font-size: 34px;
    color: var(--lime);
    letter-spacing: 0.5px;
  }
</style>
</head>
<body>
  <main class="poster">
    <svg class="marker marker-square" width="46" height="46" viewBox="0 0 46 46" aria-hidden="true">
      <rect width="46" height="46" fill="var(--lime)"/>
    </svg>
    <svg class="marker marker-arrow" width="56" height="56" viewBox="0 0 56 56" aria-hidden="true">
      <polygon points="0,0 56,28 0,56" fill="var(--lime)"/>
    </svg>
    <h1 class="headline">
      <span class="question">Having</span>
      <span class="question">trouble</span>
      <span class="question">getting</span>
      <span class="question">started?</span>
      <span class="action">Quit</span>
      <span class="action">talking</span>
      <span class="connector">and</span>
      <span class="action">start</span>
      <span class="action">doing</span>
    </h1>
    <div class="brand">Brindle Terrace</div>
  </main>
</body>
</html>
```